Real Estate Managemene Company Needs Business Card Design

We have a logo design and just need business cards made now for our business. Please use PDF logo # 3.

Card with Information to be attached shortly.

The card is used for a real estate management company. We will need to add four other employees and their cards.

Industry/Entity Type

Real Estate

Contact Information for Business Card

Tariq Hamdan
President
3187 Thornwick Avenue
Suite C
Cedar Brook, OR 97412
Phone 541.417.2286
Fax 541.417.2287
Cell 541.473.8062
vantorp@mailbreeze.net

Once design is approved we will have four other employees
Omar Hamdan
Operations Manager

Nadia Hamdan
Administrative Manager

Faz Hamdan
Principal

We would need to take out the cell # 541.473.8062 out for the remaining three cards.

Requirements
Must have
• Please use logo attached

```html
<!DOCTYPE html>
<html lang="en">
<head>
<meta charset="utf-8">
<title>Brightfield Property Management – Business Card</title>
<link rel="stylesheet" href="https://fonts.googleapis.com/css2?family=Montserrat:wght@800&family=Source+Sans+3:wght@400;600&display=swap">
<style>
  :root {
    --backdrop: #d9d9db;
    --card-charcoal: #2f3033;
    --brand-red: #e01f2d;
    --ink-white: #ffffff;
    --ink-grey: #c9cacc;
    --band-ink: #3a1013;
  }
  * { box-sizing: border-box; margin: 0; padding: 0; }
  html, body {
    width: 1200px;
    height: 800px;
    overflow: hidden;
    background: var(--backdrop);
  }
  .canvas {
    width: 1200px;
    height: 800px;
    display: flex;
    align-items: center;
    justify-content: center;
  }
  .business-card {
    position: relative;
    width: 840px;
    height: 480px;
    background: var(--card-charcoal);
    overflow: hidden;
    font-family: "Source Sans 3", Arial, sans-serif;
    box-shadow: 0 10px 28px rgba(0,0,0,.18);
  }
  .brand-block {
    position: absolute;
    left: 70px;
    top: 150px;
    width: 330px;
    display: flex;
    align-items: center;
    gap: 16px;
  }
  .brand-square {
    width: 54px;
    height: 54px;
    background: var(--brand-red);
    flex: none;
  }
  .brand-name {
    font-family: "Montserrat", Arial, sans-serif;
    font-weight: 800;
    color: var(--brand-red);
    font-size: 24px;
    line-height: 1.15;
    text-transform: uppercase;
    letter-spacing: .3px;
  }
  .person-block {
    position: absolute;
    left: 470px;
    top: 70px;
  }
  .person-name {
    font-family: "Montserrat", Arial, sans-serif;
    font-weight: 800;
    color: var(--brand-red);
    font-size: 34px;
    text-transform: uppercase;
    line-height: 1.1;
  }
  .person-title {
    color: var(--ink-white);
    font-size: 29px;
    font-weight: 400;
    margin-top: 4px;
  }
  .person-line {
    color: var(--ink-grey);
    font-size: 19px;
    line-height: 1.4;
  }
  .person-line.cell { margin-top: 6px; }
  .contact-band {
    position: absolute;
    left: 0;
    bottom: 0;
    width: 100%;
    height: 150px;
    background: var(--brand-red);
    display: flex;
    align-items: center;
    justify-content: space-between;
    padding: 30px 60px 0;
  }
  .contact-item {
    display: flex;
    align-items: center;
    gap: 12px;
    color: var(--band-ink);
    font-size: 22px;
  }
  .contact-icon { width: 24px; height: 22px; fill: var(--band-ink); flex: none; }
</style>
</head>
<body>
<main class="canvas">
  <article class="business-card">
    <div class="brand-block">
      <span class="brand-square"></span>
      <div class="brand-name">Brightfield<br>Property<br>Management</div>
    </div>

    <div class="person-block">
      <h1 class="person-name">Tariq Hamdan</h1>
      <p class="person-title">President</p>
      <p class="person-line cell">541.473.8062</p>
      <p class="person-line">3187 Thornwick Avenue Suite C,</p>
      <p class="person-line">Cedar Brook, OR 97412</p>
    </div>

    <footer class="contact-band">
      <div class="contact-item fax">
        <svg class="contact-icon" viewBox="0 0 24 22" aria-hidden="true">
          <rect x="6" y="1" width="12" height="6"/>
          <rect x="1" y="8" width="22" height="9" rx="2"/>
          <rect x="6" y="14" width="12" height="7"/>
        </svg>
        <span>541.417.2287</span>
      </div>
      <div class="contact-item email">
        <svg class="contact-icon" viewBox="0 0 24 22" aria-hidden="true">
          <path d="M1 4h22v14H1z M2 5l10 8 10-8" />
        </svg>
        <span>vantorp@mailbreeze.net</span>
      </div>
      <div class="contact-item phone">
        <svg class="contact-icon" viewBox="0 0 24 22" aria-hidden="true">
          <path d="M2 7c0-3 4-5 10-5s10 2 10 5v2h-6V7H8v2H2z"/>
          <path d="M5 12l3-3h8l3 3v8H5z"/>
        </svg>
        <span>541.417.2286</span>
      </div>
    </footer>
  </article>
</main>
</body>
</html>
```